business card/stationary design
business card/stationary
Use same font as used in my logo
Use different font if you think it looks better
Professional
Glen R. Whitmore
Managing Partner
4197-B West Harlow Creek Rd.
Cedar Hollow, TN 37190
glen.whitmore@bluelanternfinancialgroup.example
Bluelanternfinancialgroup.example
I want a clean professional looking card and simple stationary design.
nothing

```html
<!DOCTYPE html>
<html lang="en">
<head>
<meta charset="utf-8">
<title>Blue Lantern Financial Group – Stationery</title>
<link href="https://fonts.googleapis.com/css2?family=Cinzel:wght@600;700&family=Lato:wght@400;700&display=swap" rel="stylesheet">
<style>
  :root{
    --canvas:#e4e4e4;
    --paper:#ffffff;
    --maroon:#7b1d2c;
    --maroon-dark:#5c1320;
    --ink:#3c3c3c;
    --muted:#8a8a8a;
    --rule:#cfcfcf;
    --faint:#efe9e4;
  }
  *{box-sizing:border-box;margin:0;padding:0}
  html,body{width:1200px;height:559px;overflow:hidden;background:var(--canvas)}
  body{position:relative;font-family:"Lato",Arial,sans-serif;color:var(--ink)}
  address{font-style:normal}
  .sheet,.envelope,.card{position:absolute;background:var(--paper);box-shadow:0 1px 3px rgba(0,0,0,.18);overflow:hidden}
  .brand{display:flex;align-items:center;gap:5px;font-family:"Cinzel",Georgia,serif;font-weight:700;color:var(--maroon);line-height:1.1}
  .brand-dot{flex:none;border-radius:50%;background:var(--maroon)}
  .return-address{position:absolute;font-size:4.4px;line-height:1.55;color:var(--muted);text-align:left;white-space:nowrap}
  .footer-band{position:absolute;left:0;bottom:0;width:100%}
  .footer-web{position:absolute;left:18px;bottom:8px;font-size:5px;color:#fff;letter-spacing:.2px}

  /* fax */
  .fax{left:29px;top:43px;width:266px;height:473px}
  .fax .brand{position:absolute;left:18px;top:20px;font-size:10px;width:140px}
  .fax .brand-dot{width:10px;height:10px}
  .fax .return-address{right:14px;top:20px}
  .fax-title{position:absolute;left:18px;top:66px;font-family:"Cinzel",Georgia,serif;font-size:22px;font-weight:700;color:var(--ink)}
  .fax-fields{position:absolute;left:18px;top:104px;width:230px}
  .fax-row{display:flex;gap:10px}
  .fax-field{flex:1;display:flex;align-items:flex-end;height:17px;border-bottom:1px solid var(--rule);font-size:5px;color:var(--muted)}
  .fax-checks{position:absolute;left:18px;top:252px;width:230px;display:flex;justify-content:space-between;font-size:4.6px;color:var(--muted)}
  .fax-checks span{display:flex;align-items:center;gap:3px}
  .fax-checks i{display:inline-block;width:5px;height:5px;border:1px solid var(--muted)}

  /* letterhead */
  .letterhead{left:312px;top:43px;width:276px;height:473px}
  .letterhead .brand{position:absolute;left:18px;top:20px;font-size:10px;width:140px}
  .letterhead .brand-dot{width:10px;height:10px}
  .letterhead .return-address{right:14px;top:20px}
  .letter-body{position:absolute;left:18px;top:70px;width:236px;font-size:5px;line-height:1.7;color:var(--ink)}
  .letter-body p{margin-bottom:7px}
  .signature-line{display:block;width:48px;height:16px;margin:2px 0 3px}

  /* envelope */
  .envelope{left:619px;top:60px;width:552px;height:216px}
  .envelope .brand{position:absolute;left:22px;top:72px;font-size:15px;width:220px}
  .envelope .brand-dot{width:14px;height:14px}
  .envelope .return-address{left:22px;bottom:14px}
  .envelope-mark{position:absolute;right:58px;top:52px;width:130px;height:130px;border-radius:50%;background:var(--faint)}
  .stamp-box{position:absolute;right:178px;top:10px;width:12px;height:12px;border-radius:50%;background:#fff}

  /* cards */
  .card{width:211px;height:120px;top:328px}
  .card-front{left:629px}
  .card-back{left:848px}
  .card-front .brand{position:absolute;left:14px;top:28px;font-size:8px;width:130px}
  .card-front .brand-dot{width:8px;height:8px}
  .card-person{position:absolute;left:14px;top:64px;font-size:5.5px;line-height:1.5}
  .card-person strong{display:block;font-size:6.5px;color:var(--maroon)}
  .card-contact{position:absolute;right:10px;top:62px;font-size:4.2px;line-height:1.55;color:var(--muted);text-align:right;white-space:nowrap}
  .card-back .brand{position:absolute;left:50%;top:40px;transform:translateX(-50%);font-size:11px;width:170px;justify-content:center;text-align:center}
  .card-back .brand-dot{width:11px;height:11px}
</style>
</head>
<body>

<!-- Fax cover -->
<section class="sheet fax">
  <div class="brand"><span class="brand-dot"></span><span>Blue Lantern Financial Group, LLC</span></div>
  <address class="return-address">4197-B West Harlow Creek Rd.<br>Cedar Hollow, TN 37190<br>615-555-0187<br>glen.whitmore@<br>bluelanternfinancialgroup.example</address>
  <h1 class="fax-title">FAX</h1>
  <div class="fax-fields">
    <div class="fax-row"><div class="fax-field">To:</div><div class="fax-field">From:</div></div>
    <div class="fax-row"><div class="fax-field">Fax:</div><div class="fax-field">Pages:</div></div>
    <div class="fax-row"><div class="fax-field">Phone:</div><div class="fax-field">Date:</div></div>
    <div class="fax-row"><div class="fax-field">Re:</div><div class="fax-field">CC:</div></div>
    <div class="fax-row"><div class="fax-field"></div></div>
    <div class="fax-row"><div class="fax-field"></div></div>
  </div>
  <div class="fax-checks">
    <span><i></i>Urgent</span><span><i></i>For Review</span><span><i></i>Please Comment</span><span><i></i>Please Reply</span><span><i></i>Please Recycle</span>
  </div>
  <svg class="footer-band" viewBox="0 0 266 40" width="266" height="40" aria-hidden="true">
    <path d="M0 14 Q133 0 266 10 L266 40 L0 40Z" fill="var(--maroon-dark)"/>
    <path d="M0 18 Q133 6 266 14 L266 40 L0 40Z" fill="var(--maroon)"/>
  </svg>
  <span class="footer-web">www.Bluelanternfinancialgroup.example</span>
</section>

<!-- Letterhead -->
<section class="sheet letterhead">
  <div class="brand"><span class="brand-dot"></span><span>Blue Lantern Financial Group, LLC</span></div>
  <address class="return-address">4197-B West Harlow Creek Rd.<br>Cedar Hollow, TN 37190<br>615-555-0187<br>glen.whitmore@<br>bluelanternfinancialgroup.example</address>
  <div class="letter-body">
    <p>Dear Client,</p>
    <p>Thank you for your continued trust in our team. We are pleased to share an update on your accounts and the planning steps we discussed at our last meeting.</p>
    <p>Please review the enclosed summary and call our office with any questions. We look forward to working with you in the coming year.</p>
    <p>Our advisors remain ready to help you plan for every stage of life.</p>
    <p>Sincerely,
      <svg class="signature-line" viewBox="0 0 48 16" aria-hidden="true"><path d="M2 12 C8 2 12 14 18 6 S28 12 34 5 S42 10 46 8" fill="none" stroke="var(--ink)" stroke-width="1"/></svg>
      Glen R. Whitmore</p>
  </div>
  <svg class="footer-band" viewBox="0 0 276 40" width="276" height="40" aria-hidden="true">
    <path d="M0 14 Q138 0 276 10 L276 40 L0 40Z" fill="var(--maroon-dark)"/>
    <path d="M0 18 Q138 6 276 14 L276 40 L0 40Z" fill="var(--maroon)"/>
  </svg>
  <span class="footer-web">www.Bluelanternfinancialgroup.example</span>
</section>

<!-- Envelope -->
<section class="envelope">
  <svg viewBox="0 0 552 40" width="552" height="40" style="position:absolute;left:0;top:0" aria-hidden="true">
    <path d="M0 0 H552 V24 Q276 40 0 22Z" fill="var(--maroon)"/>
  </svg>
  <span class="stamp-box"></span>
  <div class="envelope-mark" role="img" aria-label="Faint brand emblem area"></div>
  <div class="brand"><span class="brand-dot"></span><span>Blue Lantern Financial Group, LLC</span></div>
  <address class="return-address">4197-B West Harlow Creek Rd. | Cedar Hollow, TN 37190 | BLFG</address>
</section>

<!-- Business card front -->
<section class="card card-front">
  <svg viewBox="0 0 211 22" width="211" height="22" style="position:absolute;left:0;top:0" aria-hidden="true">
    <path d="M0 0 H211 V12 Q105 22 0 12Z" fill="var(--maroon)"/>
  </svg>
  <div class="brand"><span class="brand-dot"></span><span>Blue Lantern Financial Group, LLC</span></div>
  <div class="card-person"><strong>Glen R. Whitmore</strong>Managing Partner</div>
  <address class="card-contact">4197-B West Harlow Creek Rd.<br>Cedar Hollow, TN 37190<br>615-555-0187<br>glen.whitmore@bluelanternfinancialgroup.example<br>Bluelanternfinancialgroup.example</address>
</section>

<!-- Business card back -->
<section class="card card-back">
  <div class="brand"><span class="brand-dot"></span><span>Blue Lantern Financial Group, LLC</span></div>
  <svg class="footer-band" viewBox="0 0 211 24" width="211" height="24" aria-hidden="true">
    <path d="M0 10 Q105 0 211 8 L211 24 L0 24Z" fill="var(--maroon)"/>
  </svg>
</section>

</body>
</html>
```